Indonesian Restaurant in Singapore Needs a Menu Design

We need a new menu design for Kopi Rindang 42's Singapore branch. We sell Indonesian fast food; our specialties are ayam penyet set meal (crispy chicken set meal), oxtail soup with rice, beefball soup noodles, chicken noodle special and our famous Kopi Rindang (ice mixed fruit) dessert. We would like pictures of our specialities (and if space and creativity permitting, other photos too) included in our menu with its name below or above it to entice customers to purchase the items. The design colours should include yellow and green and perhaps some red - similar to our logo.
Our current menu is double-sided A4-size with equal-sized photos of some of our food and drinks. We would like the menu to be larger - maybe 25x35cm double-sided or tri-fold.
The feel of our restaurant is casual and personable. The restaurant is located in a downtown mall, thus convenient for customers to visit. Our food is tasty and is served within 5 to 10 minutes. Think Burgavilla with rice and noodles served, but with personable staff.
Pictures of these food choices are uploaded. Refer to http://www.kopirindang42.example/ for our food choices. Our menu and logo is included in the file titled "Dec 15 Kopi Rindang Order sheet"

Target Market(s)

Our target customers are young people, students, Indonesians and the Malay community in Singapore.

Industry/Entity Type

Asian Restaurant

Font styles to use
Serif
Sans Serif

Requirements
Must have
• Pictures of specialties with its name above or below, yellow and green included in design. Halal logo should be in the menu.
Nice to have
• organised items for menu, with nice headings for each food category, logo included in menu.

```html
<!DOCTYPE html>
<html lang="en">
<head>
<meta charset="utf-8">
<title>Kopi Rindang 42 — Menu</title>
<link rel="stylesheet" href="https://fonts.googleapis.com/css2?family=Marcellus+SC&family=Cinzel+Decorative:wght@400;700&family=Arimo:ital,wght@0,700;1,700&display=swap">
<style>
:root{
  --cream:#ead9b8;
  --pattern:#d9cfaa;
  --green:#1c6a3c;
  --green-dark:#16512f;
  --red:#d8161e;
  --grey:#5d5d5d;
  --ink:#222;
  --brown:#3a2a17;
  --white:#fff;
}
*{margin:0;padding:0;box-sizing:border-box}
html,body{width:858px;height:1200px;overflow:hidden;background:var(--cream)}
.menu{position:relative;width:858px;height:1200px;background:var(--cream);font-family:"Arimo",sans-serif}
.abs{position:absolute}
.pattern-top{left:0;top:0;width:858px;height:214px;background:linear-gradient(var(--pattern),#d3c9a2)}
.pattern-bottom{left:0;top:1115px;width:858px;height:56px;background:var(--pattern)}
.footer-band{left:0;top:1171px;width:858px;height:29px;background:var(--brown)}
.brand{left:0;top:90px;width:858px;display:flex;justify-content:center;align-items:center;gap:12px}
.brand-dot{width:38px;height:38px;border-radius:50%;background:var(--green)}
.brand-name{font-family:"Arimo",sans-serif;font-weight:700;font-size:40px;color:var(--green)}
.order-bar{left:2px;top:214px;width:856px;height:35px;background:var(--green);color:var(--white);
  font-family:"Marcellus SC",serif;font-size:22px;display:flex;align-items:center;justify-content:center;letter-spacing:.5px}
.photo{overflow:hidden}
.photo-label{position:absolute;font-family:"Marcellus SC",serif;font-size:15px;letter-spacing:.6px}
.ph-panggang{left:0;top:251px;width:367px;height:271px;background:linear-gradient(135deg,#6b3d1c,#e9e5dc 60%,#f4f2ee)}
.ph-oxtail{left:371px;top:251px;width:487px;height:289px;background:linear-gradient(160deg,#e8e4de,#5b4a2e 45%,#e0dcd6);
  clip-path:path("M0 0 H487 V232 C420 240 300 262 150 289 L0 289 Z")}
.ph-penyet{left:595px;top:496px;width:263px;height:195px;background:linear-gradient(135deg,#d9d5cc,#a8743a 55%,#e1ddd6)}
.ph-noodle{left:595px;top:695px;width:263px;height:208px;background:linear-gradient(140deg,#d8b25a,#3a3a2e 50%,#c9a45c)}
.ph-mee{left:595px;top:907px;width:263px;height:208px;background:linear-gradient(150deg,#eee,#8a4a1f 50%,#b0662e)}
.ph-fish{left:0;top:695px;width:229px;height:168px;background:linear-gradient(135deg,#3f7a3a,#9a5a2a 50%,#c47a3f)}
.lbl-dark{color:#2b2b2b}
.lbl-light{color:#fff}
.try-tag{left:725px;top:429px;width:130px;height:27px;background:var(--red);border:2px solid var(--white);
  color:var(--white);font-weight:700;font-style:italic;font-size:16px;padding-left:22px;display:flex;align-items:center}
.section-title{font-family:"Cinzel Decorative",serif;font-weight:700;font-size:20px;color:var(--green)}
.section-note{font-style:italic;font-weight:700;font-size:13px;color:var(--ink);margin-left:4px}
.price-head{font-weight:700;font-size:13px;color:var(--ink)}
.row{position:absolute;height:20px;display:flex;align-items:center}
.box{width:36px;height:19px;background:var(--white);border-radius:3px;margin-right:10px;flex:none}
.item{font-family:"Marcellus SC",serif;font-size:14px;color:var(--grey);letter-spacing:.6px;white-space:nowrap}
.desc{font-style:italic;font-weight:700;font-size:13px;color:var(--ink);margin-left:8px;white-space:nowrap}
.price{position:absolute;font-weight:700;font-size:13.5px;color:var(--ink)}
.chili{position:absolute;width:62px;height:26px}
</style>
</head>
<body>
<main class="menu">
  <div class="abs pattern-top" role="img" aria-label="Decorative lattice pattern in sage green on cream"></div>
  <div class="abs brand"><span class="brand-dot"></span><span class="brand-name">Kopi Rindang 42</span></div>
  <div class="abs order-bar">Please place your order at the counter</div>

  <div class="abs photo ph-panggang" role="img" aria-label="Photo of grilled chicken with rice and soup">
    <span class="photo-label lbl-dark" style="left:103px;bottom:4px">Ayam Panggang Set Meal</span>
  </div>
  <div class="abs photo ph-oxtail" role="img" aria-label="Photo of oxtail soup in a clay pot with rice and chilli">
    <span class="photo-label lbl-dark" style="left:10px;top:36px;font-size:17px">Oxtail Soup with Rice</span>
  </div>
  <div class="abs try-tag">Try this</div>

  <div class="abs photo ph-penyet" role="img" aria-label="Photo of ayam penyet with crispy topping, rice and sambal">
    <span class="photo-label lbl-light" style="left:9px;bottom:5px;font-size:13px">Ayam Penyet Set Meal</span>
  </div>
  <div class="abs photo ph-noodle" role="img" aria-label="Photo of chicken noodle special with soup">
    <span class="photo-label lbl-light" style="left:9px;bottom:5px;font-size:13px">Chicken Noodle Special</span>
  </div>
  <div class="abs photo ph-mee" role="img" aria-label="Photo of mee goreng fried noodles with crackers">
    <span class="photo-label lbl-dark" style="left:9px;bottom:5px;font-size:13px">Mee Goreng</span>
  </div>
  <div class="abs photo ph-fish" role="img" aria-label="Photo of fried fish on banana leaf with sambal"></div>

  <!-- Set meal -->
  <div class="abs" style="left:51px;top:563px;display:flex;align-items:baseline">
    <span class="section-title">Set Meal</span><span class="section-note">"Set meals come with soup, rice and a small salad"</span>
  </div>
  <span class="abs price-head" style="left:546px;top:570px">$S</span>
  <div class="row" style="left:53px;top:593px"><span class="box"></span><span class="item">Fried Fish Set Meal</span></div>
  <span class="price" style="left:541px;top:595px">7.50</span>
  <div class="row" style="left:53px;top:618px"><span class="box"></span><span class="item">Ayam Penyet Set Meal</span><span class="desc">Crispy Chicken Set Meal</span></div>
  <span class="price" style="left:541px;top:620px">7.00</span>
  <div class="row" style="left:53px;top:644px"><span class="box"></span><span class="item">Ayam Panggang Set Meal</span><span class="desc">Fried Chicken Set Meal</span></div>
  <span class="price" style="left:541px;top:646px">6.00</span>

  <!-- Rice -->
  <span class="abs section-title" style="left:243px;top:712px">Rice</span>
  <span class="abs price-head" style="left:547px;top:721px">$S</span>
  <div class="row" style="left:245px;top:742px"><span class="box"></span><span class="item">Oxtail Soup with Rice,</span></div>
  <span class="price" style="left:541px;top:744px">8.00</span>
  <div class="row" style="left:245px;top:767px"><span class="box"></span><span class="item">Chicken Curry with Rice</span></div>
  <span class="price" style="left:541px;top:769px">5.50</span>
  <div class="row" style="left:245px;top:792px"><span class="box"></span><span class="item">Oxtail Fried Rice</span></div>
  <span class="price" style="left:541px;top:794px">8.00</span>
  <div class="row" style="left:245px;top:818px"><span class="box"></span><span class="item">Nasi Goreng</span><span class="desc">Fried Rice</span></div>
  <span class="price" style="left:541px;top:820px">5.00</span>

  <svg class="chili" style="left:466px;top:788px" viewBox="0 0 62 26" aria-label="Spicy option available"><path d="M6 4c6 2 12 10 20 18c-10-2-16-8-20-18z" fill="var(--red)"/><path d="M3 12l10 10M13 12L3 22" stroke="#111" stroke-width="2.5"/><path d="M38 2c4 6 10 14 20 20c-12 1-18-8-20-20z" fill="var(--red)"/><path d="M37 0l2 4" stroke="var(--green)" stroke-width="2"/></svg>
  <svg class="chili" style="left:466px;top:814px" viewBox="0 0 62 26" aria-label="Spicy option available"><path d="M6 4c6 2 12 10 20 18c-10-2-16-8-20-18z" fill="var(--red)"/><path d="M3 12l10 10M13 12L3 22" stroke="#111" stroke-width="2.5"/><path d="M38 2c4 6 10 14 20 20c-12 1-18-8-20-20z" fill="var(--red)"/><path d="M37 0l2 4" stroke="var(--green)" stroke-width="2"/></svg>

  <!-- Noodles -->
  <span class="abs section-title" style="left:51px;top:888px">Noodles</span>
  <span class="abs price-head" style="left:546px;top:896px">$S</span>
  <div class="row" style="left:53px;top:919px"><span class="box"></span><span class="item" style="margin-left:4px">Beefball Soup Noodle Special</span><span class="desc">(with fishcake &amp; dumpling)</span></div>
  <span class="price" style="left:541px;top:921px">7.00</span>
  <div class="row" style="left:53px;top:945px"><span class="box"></span><span class="item" style="margin-left:4px">Beefball Soup Noodle</span><span class="desc" style="margin-left:3px">(Circle: beehoon|noodles|mix)</span></div>
  <span class="price" style="left:541px;top:947px">5.00</span>
  <div class="row" style="left:53px;top:970px"><span class="box"></span><span class="item" style="margin-left:4px">Chicken Noodle Special</span><span class="desc">(with beefball &amp; dumpling)</span></div>
  <span class="price" style="left:541px;top:972px">6.00</span>
  <div class="row" style="left:53px;top:996px"><span class="box"></span><span class="item" style="margin-left:4px">Chicken Noodle Spicy Special</span><span class="desc" style="margin-left:4px">(with beefball soup, wanton &amp; egg)</span></div>
  <span class="price" style="left:541px;top:998px">6.00</span>
  <div class="row" style="left:53px;top:1021px"><span class="box"></span><span class="item" style="margin-left:4px">Chicken Noodle</span></div>
  <span class="price" style="left:541px;top:1023px">4.50</span>
  <div class="row" style="left:53px;top:1047px"><span class="box"></span><span class="item" style="margin-left:4px">Chicken Soto</span><span class="desc" style="margin-left:3px">(Circle: rice| beehoon|noodles)</span></div>
  <span class="price" style="left:541px;top:1049px">5.00</span>
  <div class="row" style="left:53px;top:1072px"><span class="box"></span><span class="item" style="margin-left:4px">Mee Goreng Fried Noodles</span></div>
  <span class="price" style="left:541px;top:1074px">5.00</span>

  <svg class="chili" style="left:230px;top:1015px" viewBox="0 0 62 26" aria-label="Spicy option available"><path d="M6 4c6 2 12 10 20 18c-10-2-16-8-20-18z" fill="var(--red)"/><path d="M3 12l10 10M13 12L3 22" stroke="#111" stroke-width="2.5"/><path d="M38 2c4 6 10 14 20 20c-12 1-18-8-20-20z" fill="var(--red)"/><path d="M37 0l2 4" stroke="var(--green)" stroke-width="2"/></svg>

  <div class="abs pattern-bottom" role="img" aria-label="Decorative lattice pattern in sage green on cream"></div>
  <div class="abs footer-band"></div>
</main>
</body>
</html>
```